Law Firm Needs Print Ad Redesigned

PLEASE READ THESE INSTRUCTIONS CAREFULLY, ESPECIALLY THE ATTACHMENT WITH THE HANDWRITTEN NOTES: FILE number 6. UNFORTUNATELY, DESIGNS WHICH DO NOT FOLLOW THE INSTRUCTIONS CANNOT BE CONSIDERED.

I am looking to have the attached business card sized ad redesigned to appear more professional, less cluttered, and cleaner overall.

Also, I want to use my new logo (also attached), and incorporate the headshot pic into the ad better, or not at all. How it is now does not look good, as it does not appear to really be part of the ad.

See attachments for notes on other adjustments needed.

Also, somewhere in the ad put "Board Certified as a Civil Trial Specialist by Amberline Collegium of Civic Letters" or "Board Certified Civil Trial Specialist" in larger font and Amberline Collegium of Civic Letters nearby or under it in smaller font. (Bar rules require me to put in the ad who the certifying organization is)

```html
<!DOCTYPE html>
<html lang="en">
<head>
<meta charset="utf-8">
<title>Hollis Law – Print Ad</title>
<link href="https://fonts.googleapis.com/css2?family=Cinzel:wght@600&family=Marcellus+SC&family=Sorts+Mill+Goudy&family=Arimo:ital,wght@0,700;1,400&display=swap" rel="stylesheet">
<style>
  :root {
    --page: #e8e5e1;
    --navy: #141d3d;
    --white: #ffffff;
    --blue: #3a7cc4;
    --red: #e0143c;
    --photo-dark: #1e2433;
    --photo-mid: #8b6f5e;
  }
  * { margin: 0; padding: 0; box-sizing: border-box; }
  html, body {
    width: 1200px; height: 1000px; overflow: hidden;
    background: var(--page);
  }
  .ad-card {
    position: absolute; left: 100px; top: 185px;
    width: 1000px; height: 630px;
    background: var(--navy);
    overflow: hidden;
    color: var(--white);
  }
  .brand {
    position: absolute; left: 60px; top: 42px;
    display: flex; align-items: center; gap: 28px;
  }
  .brand-mark {
    width: 96px; height: 96px;
    border: 6px solid var(--white);
    border-radius: 50%;
  }
  .brand-name {
    font-family: "Cinzel", serif; font-weight: 600;
    font-size: 104px; line-height: 1; letter-spacing: 1px;
    color: var(--white);
  }
  .swoosh { position: absolute; left: 0; top: 0; }
  .headshot {
    position: absolute; left: 0; top: 230px;
    width: 230px; height: 400px;
    background: radial-gradient(ellipse at 50% 28%, var(--photo-mid) 0 22%, transparent 40%),
                linear-gradient(180deg, var(--navy) 0%, var(--photo-dark) 55%, #2b3550 100%);
  }
  .details {
    position: absolute; left: 230px; right: 20px; top: 222px;
    text-align: center;
  }
  .practice-areas {
    font-family: "Marcellus SC", serif; font-size: 38px;
    letter-spacing: 1px; line-height: 1.1;
  }
  .certification {
    margin-top: 14px;
    font-family: "Sorts Mill Goudy", serif; font-size: 37px;
    color: var(--blue); line-height: 1.1;
  }
  .certifier {
    margin-top: 6px;
    font-family: "Sorts Mill Goudy", serif; font-size: 25px; line-height: 1.2;
  }
  .phone {
    margin-top: 14px;
    font-family: "Arimo", sans-serif; font-weight: 700;
    font-size: 54px; letter-spacing: 1px; line-height: 1.1;
  }
  .affiliation {
    margin-top: 6px;
    font-family: "Arimo", sans-serif; font-size: 29px;
    color: var(--blue); line-height: 1.2;
  }
  .website {
    margin-top: 10px;
    font-family: "Arimo", sans-serif; font-weight: 700;
    font-size: 31px; line-height: 1.2;
  }
  .tagline {
    margin-top: 8px;
    font-family: "Arimo", sans-serif; font-style: italic;
    font-size: 26px; line-height: 1.2;
  }
</style>
</head>
<body>
  <section class="ad-card">
    <div class="brand">
      <span class="brand-mark"></span>
      <span class="brand-name">Hollis Law</span>
    </div>
    <svg class="swoosh" width="1000" height="240" viewBox="0 0 1000 240" aria-hidden="true">
      <path d="M58 212 Q480 150 965 186 Q480 160 58 222 Z" fill="var(--red)"/>
    </svg>
    <div class="headshot" role="img" aria-label="Headshot of the attorney in a suit and tie"></div>
    <div class="details">
      <p class="practice-areas">Personal Injury • Civil Litigation</p>
      <p class="certification">Board Certified Civil Trial Specialist</p>
      <p class="certifier">Amberline Collegium of Civic Letters</p>
      <p class="phone">555.014.2088</p>
      <p class="affiliation">~Parishioner~</p>
      <p class="website">www.mycedarvalelawyer.com</p>
      <p class="tagline">Former Insurance Company Attorney. Now on Your Side.</p>
    </div>
  </section>
</body>
</html>
```